New Business Card Design Project

I would like to purchase a customized version of a design you have previously submitted - https://www.pixelvendro.com.au/design/58172936

I basically want this exact design but can you change the logo to reflect a R and a J. Business name is Ridgefold Joinery.

I’ve attached a rough example of how to change the logo.

```html
<!DOCTYPE html>
<html lang="en">
<head>
<meta charset="utf-8">
<title>Ridgefold Joinery – Business Card</title>
<link rel="stylesheet" href="https://fonts.googleapis.com/css2?family=Montserrat:wght@600&family=Open+Sans:wght@400;600&display=swap">
<style>
  :root {
    --backdrop: #dfe2e5;
    --card: #2a2a2a;
    --accent: #1fa3dc;
    --ink: #ffffff;
    --rule: #e6e6e6;
  }
  * { box-sizing: border-box; margin: 0; padding: 0; }
  html, body { width: 1200px; height: 800px; overflow: hidden; }
  body {
    background: var(--backdrop);
    font-family: "Open Sans", sans-serif;
    color: var(--ink);
    position: relative;
  }
  .card {
    position: absolute;
    left: 290px;
    width: 620px;
    height: 354px;
    background: var(--card);
    box-shadow: 0 6px 18px rgba(0,0,0,0.25);
    overflow: hidden;
  }
  .card--back { top: 32px; }
  .card--front { top: 414px; }

  .back-pattern {
    position: absolute; inset: 0;
    background: linear-gradient(135deg, #9a9a9a 0%, #5a5a5a 25%, #242424 55%, #151515 100%);
  }
  .back-name {
    position: absolute; left: 0; right: 0; top: 160px;
    text-align: center;
    font-family: "Montserrat", sans-serif; font-weight: 600;
    font-size: 22px; color: var(--accent); letter-spacing: 1px;
  }

  .brand {
    position: absolute; left: 34px; top: 138px;
    display: flex; align-items: center; gap: 12px;
  }
  .brand-mark { width: 26px; height: 26px; background: var(--accent); }
  .brand-name {
    font-family: "Montserrat", sans-serif; font-weight: 600;
    font-size: 24px; color: var(--accent); line-height: 1;
  }
  .divider {
    position: absolute; left: 318px; top: 104px;
    width: 2px; height: 150px; background: var(--rule);
  }
  .contact { position: absolute; left: 336px; top: 102px; }
  .person-name {
    font-family: "Montserrat", sans-serif; font-weight: 600;
    font-size: 19px; color: var(--accent);
  }
  .person-role { font-size: 14px; margin-bottom: 10px; }
  .contact-line {
    display: flex; align-items: flex-start; gap: 7px;
    font-size: 14px; line-height: 19px;
  }
  .contact-line svg { flex: none; width: 13px; height: 13px; margin-top: 3px; }
  .footer-rule {
    position: absolute; top: 300px; height: 2px; background: var(--rule);
  }
  .footer-rule--left { left: 40px; width: 150px; }
  .footer-rule--right { left: 430px; width: 150px; }
  .tagline {
    position: absolute; top: 289px; left: 190px; width: 240px;
    text-align: center; font-size: 15px; color: var(--accent);
  }
</style>
</head>
<body>
  <section class="card card--back">
    <div class="back-pattern" role="img" aria-label="Repeating brand pattern fading from silver to black"></div>
    <div class="back-name">Ridgefold Joinery</div>
  </section>

  <section class="card card--front">
    <div class="brand">
      <span class="brand-mark"></span>
      <span class="brand-name">Ridgefold Joinery</span>
    </div>
    <div class="divider"></div>
    <div class="contact">
      <div class="person-name">Daniel Hartley</div>
      <div class="person-role">Carpenter</div>
      <div class="contact-line">
        <svg viewBox="0 0 14 14" fill="none" stroke="#1fa3dc" stroke-width="1.4"><path d="M7 13s-4.5-4.6-4.5-7.5a4.5 4.5 0 0 1 9 0C11.5 8.4 7 13 7 13z"/><circle cx="7" cy="5.5" r="1.6"/></svg>
        <span>418 Timberline Road, Unit 22<br>Ashvale, CA 95410</span>
      </div>
      <div class="contact-line">
        <svg viewBox="0 0 14 14" fill="none" stroke="#1fa3dc" stroke-width="1.4"><path d="M3 1.5h2.5l1 3-1.5 1a7 7 0 0 0 3.5 3.5l1-1.5 3 1V11a1.5 1.5 0 0 1-1.5 1.5A10 10 0 0 1 1.5 3 1.5 1.5 0 0 1 3 1.5z"/></svg>
        <span>555-218-4630</span>
      </div>
      <div class="contact-line">
        <svg viewBox="0 0 14 14" fill="none" stroke="#1fa3dc" stroke-width="1.4"><rect x="1" y="3" width="12" height="8"/><path d="M1 3l6 5 6-5"/></svg>
        <span>dan@ridgefoldjoinery.com.au</span>
      </div>
      <div class="contact-line">
        <svg viewBox="0 0 14 14" fill="none" stroke="#1fa3dc" stroke-width="1.2"><circle cx="7" cy="7" r="5.8"/><ellipse cx="7" cy="7" rx="2.6" ry="5.8"/><path d="M1.2 7h11.6"/></svg>
        <span>www.ridgefoldjoinery.com.au</span>
      </div>
    </div>
    <div class="footer-rule footer-rule--left"></div>
    <div class="tagline">Fully Licensed Carpenter</div>
    <div class="footer-rule footer-rule--right"></div>
  </section>
</body>
</html>
```